Packaging for a new tea company

Hi guys we need a new packaging design for a tea company we are starting

Our competitors are leafora, zip an brew

I have uploaded pictures of our competitors for you to see the sample
The label need to be catchy

Our brand is called #JoinVividLeaf
We need two packaging designs one for Zest Brew and one for calmora

Detox - slim - cleanse

Also needs to says 14 Day Brewreset

Target Market(s)

Young people

Industry/Entity Type

It Company

Colors
000000

Requirements
Must have
• #joinvividleaf
Nice to have
• Herbal tea supplement 50gram
• Max label size 13.5cm x 16.5 cm
• Personally I like the paper brown bag as it looks like a higher quality and as the label is a sticker I think this would make the product look a lot better
Should not have
• Nothing

```html
<!DOCTYPE html>
<html lang="en">
<head>
<meta charset="utf-8">
<title>#JoinVividLeaf – 14 Day Brewreset labels</title>
<link href="https://fonts.googleapis.com/css2?family=Oswald:wght@400;500;600;700&display=swap" rel="stylesheet">
<style>
  :root {
    --canvas: #ffffff;
    --label-bg: #e6e6e6;
    --label-edge: #d6cbbd;
    --ink-green: #2f5a3b;
    --text-green: #3d5e48;
    --pink: #f29fb4;
    --lime: #8dc63f;
    --night-tag: #2aa3c3;
    --day-tag: #f7a21b;
    --ink: #222222;
    --white: #ffffff;
  }
  * { margin: 0; padding: 0; box-sizing: border-box; }
  html, body { width: 1200px; height: 550px; overflow: hidden; background: var(--canvas); }
  .canvas { position: relative; width: 1200px; height: 550px; font-family: "Oswald", "Arial Narrow", sans-serif; }

  .size-note { position: absolute; left: 1055px; top: 22px; font: 400 10px "Oswald", sans-serif; color: var(--ink); letter-spacing: .2px; }

  .label {
    position: absolute; width: 358px; height: 438px;
    background: var(--label-bg); border: 1px solid var(--label-edge);
    overflow: hidden;
  }
  .label--calmora { --accent: var(--pink); --tag: var(--night-tag); }
  .label--zest { --accent: var(--lime); --tag: var(--day-tag); }

  .label--large.label--calmora { left: 410px; top: 37px; }
  .label--large.label--zest { left: 779px; top: 37px; }
  .label--small { transform: scale(0.369); transform-origin: top left; }
  .label--small.label--calmora { left: 52px; top: 212px; }
  .label--small.label--zest { left: 235px; top: 212px; }

  .brand-name {
    position: absolute; left: 0; right: 0; top: 34px;
    text-align: center; font-weight: 700; font-size: 42px; line-height: 1;
    color: var(--ink-green); letter-spacing: .5px;
  }
  .benefits {
    position: absolute; left: 0; right: 0; top: 126px;
    text-align: center; font-weight: 500; font-size: 30px; line-height: 1;
    color: var(--text-green); letter-spacing: .3px;
  }
  .benefits .divider {
    display: inline-block; width: 7px; height: 5px; margin: 0 6px; vertical-align: middle;
    background: var(--accent);
  }
  .program-band {
    position: absolute; left: 0; right: 0; top: 214px; height: 90px;
    background: var(--accent);
    display: flex; align-items: center; justify-content: center;
  }
  .program-name {
    font-weight: 600; font-size: 40px; line-height: 1; color: var(--white); letter-spacing: .5px;
    white-space: nowrap;
  }
  .supplement {
    position: absolute; left: 0; right: 0; top: 334px;
    text-align: center; font-weight: 400; font-size: 20px; line-height: 1.2; color: var(--text-green); letter-spacing: .2px;
  }
  .variant-tag {
    position: absolute; left: 50%; top: 368px; transform: translateX(-50%);
    height: 26px; padding: 0 8px; display: flex; align-items: center; gap: 6px;
    background: var(--tag); color: var(--white); font-weight: 500; font-size: 16px; white-space: nowrap;
  }
  .variant-tag svg { width: 16px; height: 16px; }
  .net-weight {
    position: absolute; left: 0; right: 0; top: 398px;
    text-align: center; font-weight: 400; font-size: 19px; line-height: 1.2; color: var(--ink);
  }
</style>
</head>
<body>
<main class="canvas">

  <section class="label label--small label--calmora" aria-label="Calmora label preview">
    <p class="brand-name">#JOINVIVIDLEAF</p>
    <p class="benefits">DETOX<span class="divider"></span>SLIM<span class="divider"></span>CLEANSE</p>
    <div class="program-band"><p class="program-name">14 DAY BREWRESET</p></div>
    <p class="supplement">HERBAL TEA SUPPLEMENT</p>
    <p class="variant-tag"><svg viewBox="0 0 16 16"><path d="M10 2a6 6 0 1 0 4 10A5 5 0 0 1 10 2z" fill="#ffffff"/></svg>CALMORA</p>
    <p class="net-weight">50g</p>
  </section>

  <section class="label label--small label--zest" aria-label="Zest Brew label preview">
    <p class="brand-name">#JOINVIVIDLEAF</p>
    <p class="benefits">DETOX<span class="divider"></span>SLIM<span class="divider"></span>CLEANSE</p>
    <div class="program-band"><p class="program-name">14 DAY BREWRESET</p></div>
    <p class="supplement">HERBAL TEA SUPPLEMENT</p>
    <p class="variant-tag"><svg viewBox="0 0 16 16"><circle cx="8" cy="8" r="3.5" fill="#ffffff"/><g stroke="#ffffff" stroke-width="1.5" stroke-linecap="round"><path d="M8 1v2M8 13v2M1 8h2M13 8h2M3 3l1.4 1.4M11.6 11.6L13 13M3 13l1.4-1.4M11.6 4.4L13 3"/></g></svg>ZEST BREW</p>
    <p class="net-weight">50g</p>
  </section>

  <p class="size-note">13.5cm x 16.5 cm</p>

  <section class="label label--large label--calmora" aria-label="Calmora label">
    <p class="brand-name">#JOINVIVIDLEAF</p>
    <p class="benefits">DETOX<span class="divider"></span>SLIM<span class="divider"></span>CLEANSE</p>
    <div class="program-band"><p class="program-name">14 DAY BREWRESET</p></div>
    <p class="supplement">HERBAL TEA SUPPLEMENT</p>
    <p class="variant-tag"><svg viewBox="0 0 16 16"><path d="M10 2a6 6 0 1 0 4 10A5 5 0 0 1 10 2z" fill="#ffffff"/></svg>CALMORA</p>
    <p class="net-weight">50g</p>
  </section>

  <section class="label label--large label--zest" aria-label="Zest Brew label">
    <p class="brand-name">#JOINVIVIDLEAF</p>
    <p class="benefits">DETOX<span class="divider"></span>SLIM<span class="divider"></span>CLEANSE</p>
    <div class="program-band"><p class="program-name">14 DAY BREWRESET</p></div>
    <p class="supplement">HERBAL TEA SUPPLEMENT</p>
    <p class="variant-tag"><svg viewBox="0 0 16 16"><circle cx="8" cy="8" r="3.5" fill="#ffffff"/><g stroke="#ffffff" stroke-width="1.5" stroke-linecap="round"><path d="M8 1v2M8 13v2M1 8h2M13 8h2M3 3l1.4 1.4M11.6 11.6L13 13M3 13l1.4-1.4M11.6 4.4L13 3"/></g></svg>ZEST BREW</p>
    <p class="net-weight">50g</p>
  </section>

</main>
</body>
</html>
```